VORN - Business cards

Business card to be created for Commercial sales staff

Target Market(s)

Commercial businesses

Industry/Entity Type

Commercial

Contact Information for Business Card

Look professional. For commercial clients

Colors
ffffff

Requirements
Must have
• - Vorn Logo
• - Commercial sales staff as postion
• - room for commerical sales manager role
• - person name and their mobile number
• - Website : vornelectrical.com.au
Nice to have
• White background.
• On back of business card just have the logo no other information
Should not have
• Should only have white background on front of card.

```html
<!DOCTYPE html>
<html lang="en">
<head>
<meta charset="utf-8">
<title>VORN – Business cards</title>
<link rel="stylesheet" href="https://fonts.googleapis.com/css2?family=Roboto:wght@400;500;900&display=swap">
<style>
  :root {
    --stage: #e9e9ea;
    --card-front: #ffffff;
    --card-back: #212123;
    --brand-red: #c8141f;
    --ink-dark: #34363b;
    --ink-light: #ffffff;
    --radius: 28px;
  }
  * { margin: 0; padding: 0; box-sizing: border-box; }
  html, body {
    width: 1200px; height: 1000px; overflow: hidden;
    background: var(--stage);
    font-family: "Roboto", Arial, sans-serif;
  }
  .canvas { position: relative; width: 1200px; height: 1000px; }
  .card {
    position: absolute; left: 220px; width: 760px;
    border-radius: var(--radius); overflow: hidden;
    box-shadow: 0 6px 18px rgba(0,0,0,.18);
  }
  .card--front { top: 50px; height: 433px; background: var(--card-front);
    display: flex; align-items: center; justify-content: center; }
  .card--back { top: 523px; height: 435px;
    background: linear-gradient(115deg, var(--card-back) 0%, var(--card-back) 45%, #2b2b2e 62%, #1f1f21 100%); }

  .wordmark { display: flex; align-items: center; gap: 18px; }
  .wordmark__dot { border-radius: 50%; background: var(--brand-red); flex: none; }
  .wordmark__name { font-weight: 900; letter-spacing: 2px; line-height: 1; }

  .card--front .wordmark__dot { width: 56px; height: 56px; }
  .card--front .wordmark__name { font-size: 130px; color: var(--ink-dark); }

  .card--back .wordmark { position: absolute; left: 46px; top: 62px; gap: 12px; }
  .card--back .wordmark__dot { width: 34px; height: 34px; }
  .card--back .wordmark__name { font-size: 80px; color: var(--ink-light); }

  .roles { position: absolute; left: 46px; top: 207px; color: var(--ink-light);
    font-size: 17px; line-height: 27px; }
  .person { position: absolute; left: 44px; top: 292px; color: var(--brand-red);
    font-size: 22px; font-weight: 500; }
  .contact { position: absolute; left: 44px; top: 331px; list-style: none;
    color: var(--ink-light); font-size: 17px; }
  .contact__item { display: flex; align-items: center; gap: 8px; height: 28px; }
  .contact__icon { width: 12px; height: 14px; flex: none; }
</style>
</head>
<body>
<main class="canvas">
  <section class="card card--front" aria-label="Card front">
    <div class="wordmark">
      <span class="wordmark__dot"></span>
      <span class="wordmark__name">VORN</span>
    </div>
  </section>

  <section class="card card--back" aria-label="Card back">
    <div class="wordmark">
      <span class="wordmark__dot"></span>
      <span class="wordmark__name">VORN</span>
    </div>
    <p class="roles">Commercial sales staff as postion<br>Commerical sales manager role</p>
    <p class="person">Liam Carter</p>
    <ul class="contact">
      <li class="contact__item">
        <svg class="contact__icon" viewBox="0 0 12 16" aria-hidden="true">
          <rect x="1.5" y="1" width="9" height="14" rx="1.5" fill="none" stroke="#c8141f" stroke-width="1.6"/>
          <circle cx="6" cy="12.5" r="0.9" fill="#c8141f"/>
        </svg>
        012-555-0148
      </li>
      <li class="contact__item">
        <svg class="contact__icon" viewBox="0 0 16 16" aria-hidden="true">
          <circle cx="8" cy="8" r="6.5" fill="none" stroke="#c8141f" stroke-width="1.5"/>
          <ellipse cx="8" cy="8" rx="2.8" ry="6.5" fill="none" stroke="#c8141f" stroke-width="1.2"/>
          <line x1="1.5" y1="8" x2="14.5" y2="8" stroke="#c8141f" stroke-width="1.2"/>
        </svg>
        vornelectrical.com.au
      </li>
    </ul>
  </section>
</main>
</body>
</html>
```